Brand new leaflet design creative ideas.

I need a flyer designed for my business

I run a pay weekly carpet business and need designs for a flyer this design i will also want to enable it on letterheads business cards and a logo from it when created.

my domain name is www.pebblemarsh.co.uk / www.pebblemarsh.com

Our main competitor i have attached his design to this brief to give you a bit of an idea on how we work, however i do not want a copycat design i want a brand new design something not like theres but eye catching direct to the point.

We are open to colour suggestions as long as the colours work.
Thank you.

Target Market(s)

This print material will be delivered to customers houses.

Industry/Entity Type

Flooring

Font styles to use
Serif
Sans Serif

Requirements
Must have
• Website domain name,
• Various print options CMYK, PDF
Nice to have
• Creativity eye catching
Should not have
• SHOULD NOT BE A COPYCAT DESIGN SOMETHING NEW & CREATIVE

```html
<!DOCTYPE html>
<html lang="en">
<head>
<meta charset="utf-8">
<title>Pebble Marsh – Pay Weekly Carpet &amp; Vinyls Flyer</title>
<link rel="stylesheet" href="https://fonts.googleapis.com/css2?family=Lobster&family=Open+Sans:wght@400;600&family=Roboto+Condensed:wght@700&family=Alegreya:wght@500;700&family=Oswald:wght@600&display=swap">
<style>
  :root {
    --red: #e2232a;
    --yellow: #fff200;
    --green: #1a9a3a;
    --ink: #111111;
    --white: #ffffff;
    --panel: #c9cfc9;
    --room-light: #efece2;
    --room-mid: #c9c1ad;
    --carpet: #3a3a3a;
    --carpet-dark: #262626;
  }
  * { margin: 0; padding: 0; box-sizing: border-box; }
  html, body { width: 962px; height: 1200px; overflow: hidden; background: var(--white); }
  .flyer { position: relative; width: 962px; height: 1200px; overflow: hidden; font-family: "Open Sans", sans-serif; }

  .hero-photo {
    position: absolute; inset: 0;
    background:
      radial-gradient(ellipse 360px 200px at 690px 600px, #e6e1d3 0%, rgba(230,225,211,0) 100%),
      linear-gradient(180deg, var(--room-light) 0%, #e4dfd0 35%, var(--room-mid) 52%, #6b6a66 62%, var(--carpet) 75%, var(--carpet-dark) 100%);
  }
  .stripes { position: absolute; inset: 0; }

  .tagline { position: absolute; right: 22px; top: 34px; text-align: right; }
  .tagline__keep { font-family: "Alegreya", serif; font-weight: 700; font-variant: small-caps; color: var(--red); font-size: 44px; line-height: 1; letter-spacing: 0.5px; }
  .tagline__share { font-family: "Roboto Condensed", sans-serif; font-weight: 700; color: var(--ink); font-size: 40px; line-height: 1.3; letter-spacing: 0.5px; }

  .brand { position: absolute; left: 40px; top: 190px; display: flex; align-items: center; gap: 14px; }
  .brand__dot { width: 62px; height: 62px; border-radius: 50%; background: var(--red); }
  .brand__name { font-family: "Roboto Condensed", sans-serif; font-weight: 700; font-size: 54px; color: var(--red); line-height: 1; }

  .offer { position: absolute; right: 22px; top: 196px; text-align: right; }
  .offer__pay { font-family: "Lobster", cursive; font-size: 66px; color: var(--ink); line-height: 1; margin-right: 24px; }
  .offer__carpet { font-family: "Roboto Condensed", sans-serif; font-weight: 700; font-size: 62px; color: var(--red); line-height: 1; }
  .offer__amp { font-family: "Lobster", cursive; font-size: 40px; color: var(--ink); }
  .offer__vinyls { font-family: "Lobster", cursive; font-size: 64px; }

  .badge { position: absolute; border-radius: 50%; background: var(--white); border: 12px solid var(--yellow); box-shadow: 0 14px 0 0 var(--red); display: flex; flex-direction: column; align-items: center; justify-content: center; text-align: center; }
  .badge--welcome { left: 30px; top: 318px; width: 346px; height: 336px; }
  .badge--buy { left: 340px; top: 588px; width: 266px; height: 260px; }
  .badge--call { left: 672px; top: 670px; width: 282px; height: 270px; }

  .badge__welcome { font-family: "Alegreya", serif; font-weight: 700; font-variant: small-caps; color: #c8262b; font-size: 44px; line-height: 1.1; }
  .badge__area { font-family: "Roboto Condensed", sans-serif; font-weight: 700; color: var(--ink); font-size: 50px; line-height: 1.05; }
  .badge__buy { font-family: "Alegreya", serif; font-weight: 500; font-variant: small-caps; color: var(--red); font-size: 46px; line-height: 1; margin-top: -40px; }
  .badge__later { font-family: "Alegreya", serif; font-weight: 500; color: var(--ink); font-size: 44px; line-height: 1.1; }
  .badge__call { font-family: "Alegreya", serif; font-weight: 700; font-variant: small-caps; color: var(--ink); font-size: 46px; line-height: 1.1; }
  .badge__save { font-family: "Lobster", cursive; color: var(--red); font-size: 36px; line-height: 1.1; letter-spacing: 1px; }

  .deals-panel { position: absolute; inset: 0; }
  .deals { position: absolute; left: 92px; top: 696px; transform: rotate(13deg); transform-origin: left top; list-style: none; }
  .deals__title { font-family: "Oswald", sans-serif; font-weight: 600; font-size: 27px; color: var(--ink); line-height: 34px; margin: 0 0 4px -12px; letter-spacing: 0.3px; white-space: nowrap; }
  .deals__item { font-size: 27px; color: var(--red); line-height: 41px; display: flex; align-items: center; gap: 9px; padding-left: 2px; white-space: nowrap; }
  .deals__tick { width: 15px; height: 15px; flex: none; }

  .contact { position: absolute; left: 528px; top: 1038px; width: 434px; height: 133px; background: var(--yellow); padding: 14px 18px 0 18px; }
  .contact__row { display: flex; align-items: center; gap: 10px; font-family: "Roboto Condensed", sans-serif; font-weight: 700; color: var(--red); }
  .contact__row--phone { font-size: 48px; line-height: 1.1; }
  .contact__row--web { font-size: 31px; line-height: 1.4; margin-left: 6px; }
  .contact__icon { width: 40px; height: 40px; flex: none; }
</style>
</head>
<body>
<div class="flyer">
  <div class="hero-photo" role="img" aria-label="Photo of a bright living room with a mother and daughter lying on a soft cream carpet, dark carpet in the foreground"></div>

  <svg class="stripes" width="962" height="1200" viewBox="0 0 962 1200" aria-hidden="true">
    <path d="M0 268 Q 360 590 962 780" fill="none" stroke="var(--yellow)" stroke-width="12"/>
    <path d="M0 284 Q 360 606 962 796" fill="none" stroke="var(--green)" stroke-width="12"/>
    <path d="M0 300 Q 360 622 962 812" fill="none" stroke="var(--red)" stroke-width="12"/>
  </svg>

  <svg class="deals-panel" width="962" height="1200" viewBox="0 0 962 1200" aria-hidden="true">
    <polygon points="0,665 517,762 411,1151 0,1069" fill="var(--panel)"/>
  </svg>

  <div class="tagline">
    <p class="tagline__keep">Keep This Flyer Safe or</p>
    <p class="tagline__share">SHARE WITH YOUR BUDDIES</p>
  </div>

  <div class="brand">
    <span class="brand__dot"></span>
    <span class="brand__name">Pebble Marsh</span>
  </div>

  <div class="offer">
    <p class="offer__pay">Pay Weekly</p>
    <p class="offer__carpet">CARPET <span class="offer__amp">&amp;</span> <span class="offer__vinyls">Vinyls</span></p>
  </div>

  <div class="badge badge--welcome">
    <p class="badge__welcome">Welcome!</p>
    <p class="badge__area">WE’RE IN<br>YOUR AREA</p>
  </div>

  <div class="badge badge--buy">
    <p class="badge__buy">Buy Now</p>
    <p class="badge__later">Pay Later</p>
  </div>

  <div class="badge badge--call">
    <p class="badge__call">Call Today</p>
    <p class="badge__save">SAVE TODAY</p>
  </div>

  <ul class="deals">
    <li class="deals__title">OUR AMAZING CARPET DEALS</li>
    <li class="deals__item"><svg class="deals__tick" viewBox="0 0 16 16"><rect x="1" y="1" width="14" height="14" fill="none" stroke="var(--red)" stroke-width="2"/><path d="M4 8l3 3 5-6" fill="none" stroke="var(--red)" stroke-width="2"/></svg>Pay only £10.00/week</li>
    <li class="deals__item"><svg class="deals__tick" viewBox="0 0 16 16"><rect x="1" y="1" width="14" height="14" fill="none" stroke="var(--red)" stroke-width="2"/><path d="M4 8l3 3 5-6" fill="none" stroke="var(--red)" stroke-width="2"/></svg>£500 credit limit</li>
    <li class="deals__item"><svg class="deals__tick" viewBox="0 0 16 16"><rect x="1" y="1" width="14" height="14" fill="none" stroke="var(--red)" stroke-width="2"/><path d="M4 8l3 3 5-6" fill="none" stroke="var(--red)" stroke-width="2"/></svg>Interest FREE</li>
    <li class="deals__item"><svg class="deals__tick" viewBox="0 0 16 16"><rect x="1" y="1" width="14" height="14" fill="none" stroke="var(--red)" stroke-width="2"/><path d="M4 8l3 3 5-6" fill="none" stroke="var(--red)" stroke-width="2"/></svg>NO Credit Checks</li>
    <li class="deals__item"><svg class="deals__tick" viewBox="0 0 16 16"><rect x="1" y="1" width="14" height="14" fill="none" stroke="var(--red)" stroke-width="2"/><path d="M4 8l3 3 5-6" fill="none" stroke="var(--red)" stroke-width="2"/></svg>FREE Underlay</li>
    <li class="deals__item"><svg class="deals__tick" viewBox="0 0 16 16"><rect x="1" y="1" width="14" height="14" fill="none" stroke="var(--red)" stroke-width="2"/><path d="M4 8l3 3 5-6" fill="none" stroke="var(--red)" stroke-width="2"/></svg>FREE Grippers</li>
    <li class="deals__item"><svg class="deals__tick" viewBox="0 0 16 16"><rect x="1" y="1" width="14" height="14" fill="none" stroke="var(--red)" stroke-width="2"/><path d="M4 8l3 3 5-6" fill="none" stroke="var(--red)" stroke-width="2"/></svg>FREE Door Trims</li>
    <li class="deals__item"><svg class="deals__tick" viewBox="0 0 16 16"><rect x="1" y="1" width="14" height="14" fill="none" stroke="var(--red)" stroke-width="2"/><path d="M4 8l3 3 5-6" fill="none" stroke="var(--red)" stroke-width="2"/></svg>FREE Home Measuring</li>
  </ul>

  <div class="contact">
    <p class="contact__row contact__row--phone">
      <svg class="contact__icon" viewBox="0 0 40 40" aria-hidden="true"><circle cx="20" cy="20" r="19" fill="var(--red)"/><path d="M11 16c0-4 18-4 18 0v2h-5v-2h-8v2h-5z M13 20h14l2 9H11z" fill="var(--white)"/><circle cx="20" cy="25" r="3" fill="var(--red)"/></svg>
      +1 800 555 0142
    </p>
    <p class="contact__row contact__row--web">
      <svg class="contact__icon" viewBox="0 0 40 40" aria-hidden="true"><circle cx="20" cy="20" r="18" fill="var(--red)"/><g fill="none" stroke="var(--white)" stroke-width="2"><circle cx="20" cy="20" r="11"/><ellipse cx="20" cy="20" rx="5" ry="11"/><path d="M9 20h22M11 14h18M11 26h18"/></g></svg>
      www.pebblemarsh.co.uk
    </p>
  </div>
</div>
</body>
</html>
```